EPIC, awesome, creative business card needed - get involved!

I'm launching a boutique, exclusive Property Management real estate agency in Sydney early next year.
The name of the agency will be called "Quartz Hill Lane" - it's a play on "chase the silver pebble trail" to wealth. The Quartz Hill Lane signifies wealth through property investment.
My business will offer management of investment properties (ie Property Management).
The difference with Quartz Hill Lane and other agencies is the business will be run by one of Australia's leading property investment experts, and also one of Australia's leading property managers.
It will be exclusively for high net worth properties and individuals, so the business card needs to be extremely sharp, slick and relatively simple.
The information I want on the card is as follows
Nolan Pryce - Director
M: 0412 967 154
P: 9735 6021
E: nolan@quartzhilllane.net.au
W: quartzhilllane.net.au
I'm happy with the red from the logo, black - no yellows or funky colors. I want this to be a super corporate and slick business card to match the high end nature of the business.
Good luck everyone, and please ask questions for clarification.

```html
<!DOCTYPE html>
<html lang="en">
<head>
<meta charset="utf-8">
<title>Quartz Hill Lane – Business Card</title>
<link rel="stylesheet" href="https://fonts.googleapis.com/css2?family=Oswald:wght@500;700&family=Open+Sans:wght@400;600&display=swap">
<style>
  :root {
    --page: #3a3a3c;
    --card-black: #1a1a1b;
    --card-panel: #1e1e1f;
    --ghost: #252526;
    --red: #c3161c;
    --red-light: #d8242a;
    --red-deep: #9c1418;
    --silver: #e3e4e6;
    --charcoal: #202021;
    --ink: #1a1a1b;
    --text-light: #e8e8e8;
    --text-soft: #cfcfcf;
  }
  * { box-sizing: border-box; margin: 0; padding: 0; }
  html, body { width: 1200px; height: 900px; overflow: hidden; }
  body {
    background: var(--page);
    font-family: "Open Sans", Arial, sans-serif;
    position: relative;
  }
  .card {
    position: absolute;
    top: 301px;
    width: 520px;
    height: 297px;
    border-radius: 3px;
    overflow: hidden;
    box-shadow: 0 10px 30px rgba(0,0,0,0.45);
  }
  .card--front { left: 50px; }
  .card--back { left: 630px; background: var(--card-black); }

  .front-art {
    position: absolute;
    inset: 0;
    background: linear-gradient(172deg,
      var(--red-light) 0%,
      var(--red-deep) 34%,
      var(--silver) 46%,
      var(--silver) 56%,
      var(--charcoal) 72%,
      var(--card-black) 100%);
  }
  .front-brand {
    position: absolute;
    top: 122px;
    left: 0; right: 0;
    display: flex;
    justify-content: center;
    align-items: center;
    gap: 10px;
  }
  .brand-square { width: 22px; height: 22px; background: var(--red); flex: none; }
  .brand-name {
    font-family: "Oswald", Arial, sans-serif;
    font-weight: 700;
    font-size: 20px;
    letter-spacing: 1px;
    text-transform: uppercase;
    color: var(--ink);
    white-space: nowrap;
  }

  .back-panel {
    position: absolute;
    top: 0; bottom: 0;
    left: 150px; width: 150px;
    background: var(--card-panel);
  }
  .ghost-name {
    position: absolute;
    left: 28px;
    top: 18px;
    font-family: "Oswald", Arial, sans-serif;
    font-weight: 700;
    font-size: 50px;
    line-height: 0.98;
    text-transform: uppercase;
    color: var(--ghost);
  }
  .back-brand {
    position: absolute;
    left: 36px;
    bottom: 34px;
    display: flex;
    align-items: center;
    gap: 12px;
  }
  .back-brand .brand-square { width: 54px; height: 54px; }
  .back-brand .brand-name { color: var(--text-light); font-size: 18px; }

  .person {
    position: absolute;
    left: 206px;
    top: 92px;
  }
  .person-name {
    font-family: "Oswald", Arial, sans-serif;
    font-weight: 500;
    font-size: 21px;
    letter-spacing: 0.5px;
    text-transform: uppercase;
    color: var(--text-light);
    line-height: 1.1;
  }
  .person-role {
    font-size: 11px;
    color: var(--red-light);
    margin-bottom: 6px;
  }
  .contact-list { list-style: none; }
  .contact-list li {
    display: flex;
    align-items: center;
    gap: 6px;
    font-size: 10.5px;
    color: var(--text-soft);
    line-height: 1.7;
    white-space: nowrap;
  }
  .contact-list svg { width: 10px; height: 10px; fill: var(--red-light); flex: none; }
  .contact-list--web {
    position: absolute;
    left: 340px;
    top: 96px;
  }
  .contact-list--web li { font-size: 9.5px; }
</style>
</head>
<body>

  <section class="card card--front" aria-label="Card front">
    <div class="front-art" role="img" aria-label="Decorative sweep of red, silver and charcoal bands"></div>
    <div class="front-brand">
      <span class="brand-square"></span>
      <span class="brand-name">Quartz Hill Lane</span>
    </div>
  </section>

  <section class="card card--back" aria-label="Card back">
    <div class="back-panel"></div>
    <div class="ghost-name" aria-hidden="true">Quartz<br>Hill<br>Lane</div>

    <div class="back-brand">
      <span class="brand-square"></span>
      <span class="brand-name">Quartz Hill Lane</span>
    </div>

    <div class="person">
      <p class="person-name">Nolan Pryce</p>
      <p class="person-role">Director</p>
      <ul class="contact-list">
        <li>
          <svg viewBox="0 0 10 10"><path d="M1 3 Q1 1 3 1 L7 1 Q9 1 9 3 L9 4 L7 4 L7 3 L3 3 L3 4 L1 4 Z M2 5 L8 5 L9 9 L1 9 Z"/></svg>
          9735 6021
        </li>
        <li>
          <svg viewBox="0 0 10 10"><path d="M3 0 H7 Q8 0 8 1 V9 Q8 10 7 10 H3 Q2 10 2 9 V1 Q2 0 3 0 Z M3 1.5 V7.5 H7 V1.5 Z"/></svg>
          0412 967 154
        </li>
      </ul>
    </div>

    <ul class="contact-list contact-list--web">
      <li>
        <svg viewBox="0 0 10 10"><path d="M5 0 A5 5 0 1 0 5 10 A5 5 0 1 0 5 0 Z M5 1 A4 4 0 0 1 9 5 H6.5 Q6.4 2.5 5 1 Z M5 1 Q3.6 2.5 3.5 5 H1 A4 4 0 0 1 5 1 Z M1 5.6 H3.5 Q3.6 7.6 5 9 A4 4 0 0 1 1 5.6 Z M6.5 5.6 H9 A4 4 0 0 1 5 9 Q6.4 7.6 6.5 5.6 Z"/></svg>
        www.quartzhilllane.net.au
      </li>
      <li>
        <svg viewBox="0 0 10 10"><path d="M0 2 H10 V8 H0 Z M0.8 2.6 L5 5.6 L9.2 2.6 Z" fill-rule="evenodd"/></svg>
        nolan@quartzhilllane.net.au
      </li>
    </ul>
  </section>

</body>
</html>
```